Business card for STEADYLINE

Please design professional business card for IT consulting firm STEADYLINE INC.
Use logo attached.
Use information from sample tRove business card attached.
replace trove inc with STEADYLINE INC.
as well as troveinc.com with steadyline.example

```html
<!DOCTYPE html>
<html lang="en">
<head>
<meta charset="utf-8">
<title>STEADYLINE Business Card</title>
<link rel="stylesheet" href="https://fonts.googleapis.com/css2?family=Montserrat:wght@400;500;600;700&display=swap">
<style>
  :root {
    --bg: #c4c4c4;
    --paper: #ffffff;
    --ink: #141414;
    --dark: #242424;
    --dark-soft: #3a3a3a;
    --teal: #2ee6c8;
    --blue: #5b86e8;
    --purple: #9a16d8;
    --orange: #f08a24;
    --white: #ffffff;
  }
  * { box-sizing: border-box; margin: 0; padding: 0; }
  html, body {
    width: 1200px; height: 800px; overflow: hidden;
    background: var(--bg);
    font-family: "Montserrat", sans-serif;
    color: var(--ink);
  }
  .stage {
    width: 1200px; height: 800px;
    display: flex; flex-direction: column;
    align-items: center; justify-content: center; gap: 40px;
  }
  .card {
    position: relative;
    width: 560px; height: 320px;
    box-shadow: 0 10px 24px rgba(0,0,0,0.22);
  }
  .card--front { background: var(--paper); }
  .wordmark {
    position: absolute; left: 0; right: 0; top: 52px;
    text-align: center;
    font-size: 42px; font-weight: 600; letter-spacing: 7px;
    color: var(--ink);
  }
  .wordmark__square {
    display: inline-block; width: 14px; height: 14px;
    background: var(--ink); margin-left: 6px; vertical-align: 24px;
  }
  .divider {
    position: absolute; left: 36px; right: 36px; top: 170px;
    height: 2px; display: flex;
  }
  .divider span { flex: 1; }
  .divider .teal { background: var(--teal); }
  .divider .blue { background: var(--blue); }
  .divider .purple { background: var(--purple); }
  .divider .orange { background: var(--orange); }
  .person {
    position: absolute; left: 36px; top: 128px;
    line-height: 1.25;
  }
  .person__name { font-size: 15px; font-weight: 700; letter-spacing: 0.2px; }
  .person__name small { font-size: 15px; font-weight: 500; }
  .person__role { font-size: 14px; font-weight: 400; }
  .contacts {
    position: absolute; left: 36px; top: 184px;
    list-style: none; font-size: 14px; line-height: 23px;
  }
  .contacts li { display: flex; align-items: center; gap: 8px; }
  .contacts svg { width: 14px; height: 14px; flex: none; }
  .company {
    position: absolute; right: 36px; top: 184px;
    text-align: right; font-size: 14px; line-height: 21px;
  }
  .company__name { font-weight: 700; }
  .card--back { background: var(--dark); overflow: hidden; }
  .back-texture {
    position: absolute; inset: 0;
    background: linear-gradient(150deg, var(--dark-soft) 0%, var(--dark) 55%, #151515 100%);
  }
  .back-wordmark {
    position: absolute; left: 0; right: 0; top: 140px;
    text-align: center;
    font-size: 34px; font-weight: 600; letter-spacing: 6px;
    color: var(--white);
  }
</style>
</head>
<body>
<main class="stage">
  <section class="card card--front">
    <div class="wordmark">STEADYLINE<span class="wordmark__square"></span></div>
    <div class="person">
      <div class="person__name">DANIEL MARCHETTI<small>, P.ENG.</small></div>
      <div class="person__role">General Manager</div>
    </div>
    <div class="divider"><span class="teal"></span><span class="blue"></span><span class="purple"></span><span class="orange"></span></div>
    <ul class="contacts">
      <li><svg viewBox="0 0 14 14"><rect x="3" y="1" width="8" height="12" rx="1.5" fill="none" stroke="currentColor" stroke-width="1.4"/></svg>(555)214-0370 ext.201</li>
      <li><svg viewBox="0 0 14 14"><path d="M3 2l2.5 0 1 3-1.5 1a7 7 0 0 0 3 3l1-1.5 3 1V11a1.5 1.5 0 0 1-1.5 1.5A9.5 9.5 0 0 1 1.5 3.5 1.5 1.5 0 0 1 3 2z" fill="currentColor"/></svg>(555)638-1092</li>
      <li><svg viewBox="0 0 14 14"><rect x="1" y="3" width="12" height="8" fill="currentColor"/><path d="M1 3l6 4.5L13 3" fill="none" stroke="#fff" stroke-width="1.2"/></svg>dmarchetti@steadyline.example</li>
      <li><svg viewBox="0 0 14 14"><g fill="none" stroke="currentColor" stroke-width="1.2"><circle cx="7" cy="7" r="5.8"/><ellipse cx="7" cy="7" rx="2.6" ry="5.8"/><path d="M1.2 7h11.6M2 4h10M2 10h10"/></g></svg>www.steadyline.example</li>
    </ul>
    <div class="company">
      <div class="company__name">STEADYLINE INC.</div>
      <div>1820 Harbourview Rd., Suite 101</div>
      <div>Lakeport, Ontario</div>
      <div>L4X2B9, Canada</div>
    </div>
  </section>

  <section class="card card--back">
    <div class="back-texture" role="img" aria-label="Dark embossed repeating brand pattern"></div>
    <div class="back-wordmark">STEADYLINE</div>
  </section>
</main>
</body>
</html>
```